Customer Dashboard Design for Email Security SaaS

Mailbrook is a commercial email spam filter offered as a SaaS product, built and operated by a small German hosting provider. It protects business email accounts against spam, phishing, scam, and viruses using a multilayer filtering pipeline that combines traditional spam detection with AI-powered classification. The product runs entirely on German infrastructure, ensuring data sovereignty for European customers.

We need a complete redesign of the customer-facing dashboard. This is the web application where paying customers manage their email filtering: view their mail log, check quarantined emails, manage allow/blocklists, configure their settings, and handle their subscription. It is the primary touchpoint between Mailbrook and its customers.

Our customers are system administrators, IT managers at small-to-medium businesses, and operators of small hosting providers. They are technically competent but not designers. They expect professional, efficient tools that respect their time. They typically manage 10–500 email accounts and check the dashboard a few times per week, with heavier use during spam incidents.

We have attached the current mockups which really need to be replaced with something good looking.

Target Market(s)

System administrators, IT managers at small-to-medium businesses, and operators of small hosting providers.

Industry/Entity Type

SaaS

Number of Pages Required

5+ page

```html
<!DOCTYPE html>
<html lang="en">
<head>
<meta charset="utf-8">
<title>Mailbrook – Dashboard</title>
<link href="https://fonts.googleapis.com/css2?family=Fraunces:opsz,wght@9..144,600;9..144,700&family=DM+Sans:wght@400;500&display=swap" rel="stylesheet">
<style>
:root{
  --bg:#19130f;
  --sidebar:#1c1612;
  --card:#221b16;
  --card-hi:#2a2119;
  --border:#3a2e24;
  --orange:#e8922a;
  --red:#e0312f;
  --text:#f3ece4;
  --muted:#a89a8c;
  --grid:#3d3222;
}
*{box-sizing:border-box;margin:0;padding:0}
html,body{width:1200px;height:999px;overflow:hidden;background:var(--bg);color:var(--text);font-family:"DM Sans",sans-serif}
.serif{font-family:"Fraunces",serif;font-weight:600}
.sidebar{position:absolute;left:0;top:0;width:200px;height:736px;background:var(--sidebar);border-right:1px solid var(--border)}
.brand{height:69px;display:flex;align-items:center;gap:10px;padding-left:19px;border-bottom:1px solid var(--border)}
.brand-mark{width:31px;height:31px;border-radius:8px;background:var(--orange)}
.brand-name{font-family:"Fraunces",serif;font-weight:600;font-size:16px}
.nav{padding:13px 12px 0}
.nav-item{height:37px;margin-bottom:3.6px;display:flex;align-items:center;gap:10px;padding-left:13px;font-size:12.5px;border-radius:7px;color:var(--text)}
.nav-item svg{width:14px;height:14px;stroke:currentColor;fill:none;stroke-width:1.8;stroke-linecap:round;stroke-linejoin:round}
.nav-item.active{background:var(--orange);color:#2a1a08}
.sidebar-foot{position:absolute;left:0;right:0;top:577px;border-top:1px solid var(--border);padding:0 12px}
.sidebar-foot .nav-item{margin-top:12px}
.user-card{margin-top:8px;background:#2c231c;border-radius:8px;padding:10px 13px;height:47px}
.user-card .name{font-size:11px}
.user-card .mail{font-size:9px;color:var(--muted);margin-top:2px}
.main{position:absolute;left:226px;top:0;width:948px}
h1{font-size:30px;margin-top:23px;line-height:36px}
.subtitle{font-size:12px;color:var(--muted);margin-top:3px}
.hero{margin-top:23px;height:141px;border:1px solid #4a361f;border-radius:12px;background:linear-gradient(160deg,#3a2715 0%,#231a13 60%);padding:26px 25px}
.label-caps{font-size:10px;letter-spacing:.4px;color:var(--muted)}
.hero-num{font-size:46px;line-height:52px;margin-top:4px}
.delta{font-size:10.5px;color:var(--orange);display:flex;align-items:center;gap:5px;margin-top:2px}
.stats{margin-top:26px;display:grid;grid-template-columns:repeat(5,179px);gap:13.25px}
.stat{height:135px;background:var(--card);border:1px solid var(--border);border-radius:11px;padding:19px}
.stat-icon{width:37px;height:37px;border-radius:8px;display:flex;align-items:center;justify-content:center}
.stat-icon svg{width:15px;height:15px;fill:none;stroke-width:1.8;stroke-linecap:round;stroke-linejoin:round}
.stat-num{font-size:24px;margin-top:13px;line-height:30px}
.stat-label{font-size:11px;color:var(--muted);margin-top:3px}
.chart-card{position:relative;margin-top:26px;height:407px;background:var(--card);border:1px solid var(--border);border-radius:11px;padding:20px 19px}
.chart-card h2{font-size:19px;line-height:24px}
.chart-card .subtitle{font-size:11px;margin-top:6px}
.chart{position:absolute;left:39px;top:81px}
.chart text{font-family:"DM Sans",sans-serif;font-size:12px;fill:var(--muted)}
.legend{position:absolute;left:19px;right:19px;top:352px;border-top:1px solid var(--border);padding-top:20px;display:flex;gap:13px;font-size:11px;color:var(--muted)}
.legend span{display:flex;align-items:center;gap:6px}
.legend i{width:9px;height:9px;border-radius:50%;display:inline-block}
.actions{margin-top:26px;display:grid;grid-template-columns:467px 467px;gap:14px}
.action{position:relative;height:106px;background:var(--card);border:1px solid var(--border);border-radius:11px;padding:19px}
.action svg.ic{width:17px;height:17px;stroke:var(--orange);fill:none;stroke-width:1.8;stroke-linecap:round;stroke-linejoin:round}
.action .arrow{position:absolute;right:27px;top:26px;width:11px;height:11px;stroke:var(--muted);fill:none;stroke-width:1.8;stroke-linecap:round}
.action h3{font-size:15px;margin-top:11px}
.action p{font-size:11px;color:var(--muted);margin-top:5px}
</style>
</head>
<body>
<aside class="sidebar">
  <div class="brand"><span class="brand-mark"></span><span class="brand-name">Mailbrook</span></div>
  <nav class="nav">
    <div class="nav-item active"><svg viewBox="0 0 24 24"><rect x="3" y="3" width="7" height="9"/><rect x="14" y="3" width="7" height="5"/><rect x="14" y="12" width="7" height="9"/><rect x="3" y="16" width="7" height="5"/></svg>Dashboard</div>
    <div class="nav-item"><svg viewBox="0 0 24 24"><path d="M14 2H6a2 2 0 0 0-2 2v16a2 2 0 0 0 2 2h12a2 2 0 0 0 2-2V8z"/><path d="M14 2v6h6M8 13h8M8 17h8"/></svg>Mail Log</div>
    <div class="nav-item"><svg viewBox="0 0 24 24"><path d="M22 12h-6l-2 3h-4l-2-3H2"/><path d="M5.5 5h13L22 12v6a2 2 0 0 1-2 2H4a2 2 0 0 1-2-2v-6z"/></svg>Mailboxes</div>
    <div class="nav-item"><svg viewBox="0 0 24 24"><path d="M12 22s8-4 8-10V5l-8-3-8 3v7c0 6 8 10 8 10z"/></svg>Allowlist</div>
    <div class="nav-item"><svg viewBox="0 0 24 24"><path d="M12 22s8-4 8-10V5l-8-3-8 3v7c0 6 8 10 8 10z"/><path d="M3 3l18 18"/></svg>Blocklist</div>
    <div class="nav-item"><svg viewBox="0 0 24 24"><rect x="2" y="3" width="20" height="5"/><path d="M4 8v12h16V8M10 12h4"/></svg>Quarantine</div>
    <div class="nav-item"><svg viewBox="0 0 24 24"><circle cx="12" cy="12" r="3"/><path d="M12 2v3M12 19v3M4.9 4.9l2.1 2.1M17 17l2.1 2.1M2 12h3M19 12h3M4.9 19.1L7 17M17 7l2.1-2.1"/></svg>Settings</div>
    <div class="nav-item"><svg viewBox="0 0 24 24"><rect x="2" y="5" width="20" height="14" rx="2"/><path d="M2 10h20"/></svg>Billing</div>
  </nav>
  <div class="sidebar-foot">
    <div class="nav-item"><svg viewBox="0 0 24 24"><circle cx="12" cy="12" r="4"/><path d="M12 2v2M12 20v2M4.9 4.9l1.4 1.4M17.7 17.7l1.4 1.4M2 12h2M20 12h2M4.9 19.1l1.4-1.4M17.7 6.3l1.4-1.4"/></svg>Light Mode</div>
    <div class="user-card"><div class="name">Admin User</div><div class="mail">admin@example.com</div></div>
    <div class="nav-item"><svg viewBox="0 0 24 24"><path d="M9 21H5a2 2 0 0 1-2-2V5a2 2 0 0 1 2-2h4M16 17l5-5-5-5M21 12H9"/></svg>Logout</div>
  </div>
</aside>

<main class="main">
  <h1 class="serif">Good morning, Admin</h1>
  <p class="subtitle">Here's what's happening with your email security today.</p>

  <section class="hero">
    <div class="label-caps">TOTAL EMAILS FILTERED</div>
    <div class="hero-num serif">1,719</div>
    <div class="delta"><svg width="12" height="12" viewBox="0 0 24 24" fill="none" stroke="currentColor" stroke-width="2" stroke-linecap="round"><path d="M2 17l7-7 4 4 8-8M15 6h6v6"/></svg>+12% from last week</div>
  </section>

  <section class="stats">
    <div class="stat"><div class="stat-icon" style="background:#3a2a18"><svg viewBox="0 0 24 24" stroke="var(--orange)"><path d="M12 22s8-4 8-10V5l-8-3-8 3v7c0 6 8 10 8 10z"/></svg></div><div class="stat-num serif">1,247</div><div class="stat-label">Spam Blocked</div></div>
    <div class="stat"><div class="stat-icon" style="background:#3b1a16"><svg viewBox="0 0 24 24" stroke="var(--red)"><path d="M10.3 3.9L1.8 18a2 2 0 0 0 1.7 3h17a2 2 0 0 0 1.7-3L13.7 3.9a2 2 0 0 0-3.4 0zM12 9v4M12 17h.01"/></svg></div><div class="stat-num serif">89</div><div class="stat-label">Phishing Detected</div></div>
    <div class="stat"><div class="stat-icon" style="background:#3b2216"><svg viewBox="0 0 24 24" stroke="#e5602a"><rect x="8" y="6" width="8" height="14" rx="4"/><path d="M9 3l2 3M15 3l-2 3M3 9h5M16 9h5M3 14h5M16 14h5M4 19l4-2M20 19l-4-2"/></svg></div><div class="stat-num serif">12</div><div class="stat-label">Viruses Caught</div></div>
    <div class="stat"><div class="stat-icon" style="background:#3a2a18"><svg viewBox="0 0 24 24" stroke="#f0a53a"><rect x="2" y="4" width="20" height="16" rx="2"/><path d="M22 6l-10 7L2 6"/></svg></div><div class="stat-num serif">324</div><div class="stat-label">Newsletters Sorted</div></div>
    <div class="stat"><div class="stat-icon" style="background:#3a2c20"><svg viewBox="0 0 24 24" stroke="#e9b27a"><rect x="2" y="3" width="20" height="5"/><path d="M4 8v12h16V8M10 12h4"/></svg></div><div class="stat-num serif">47</div><div class="stat-label">In Quarantine</div></div>
  </section>

  <section class="chart-card">
    <h2 class="serif">Email Volume Trend</h2>
    <p class="subtitle">Last 7 days of email filtering activity</p>
    <svg class="chart" width="897" height="250" viewBox="340 660 1150 320" role="img" aria-label="Line chart of email volume, Apr 7 to Apr 14">
      <defs>
        <linearGradient id="area" x1="0" y1="0" x2="0" y2="1">
          <stop offset="0" stop-color="#0f0b09" stop-opacity=".85"/>
          <stop offset="1" stop-color="#0f0b09" stop-opacity=".1"/>
        </linearGradient>
      </defs>
      <g stroke="var(--grid)" stroke-dasharray="3 3" stroke-width="1">
        <line x1="380" y1="669" x2="1475" y2="669"/>
        <line x1="380" y1="740" x2="1475" y2="740"/>
        <line x1="380" y1="810" x2="1475" y2="810"/>
        <line x1="380" y1="880" x2="1475" y2="880"/>
        <line x1="536" y1="669" x2="536" y2="949"/>
        <line x1="692" y1="669" x2="692" y2="949"/>
        <line x1="849" y1="669" x2="849" y2="949"/>
        <line x1="1005" y1="669" x2="1005" y2="949"/>
        <line x1="1162" y1="669" x2="1162" y2="949"/>
        <line x1="1318" y1="669" x2="1318" y2="949"/>
        <line x1="1475" y1="669" x2="1475" y2="949"/>
      </g>
      <path d="M380 792 C432 780 484 768 536 768 C588 768 640 817 692 817 C744 817 797 736 849 736 C901 736 953 782 1005 782 C1057 782 1110 757 1162 757 C1214 757 1266 802 1318 802 C1370 802 1423 772 1475 747 L1475 949 L380 949 Z" fill="url(#area)"/>
      <path d="M380 792 C432 780 484 768 536 768 C588 768 640 817 692 817 C744 817 797 736 849 736 C901 736 953 782 1005 782 C1057 782 1110 757 1162 757 C1214 757 1266 802 1318 802 C1370 802 1423 772 1475 747" fill="none" stroke="var(--red)" stroke-width="2"/>
      <g stroke="#8a7c6e" stroke-width="1">
        <line x1="380" y1="669" x2="380" y2="949"/>
        <line x1="380" y1="949" x2="1475" y2="949"/>
        <line x1="374" y1="676" x2="380" y2="676"/><line x1="374" y1="740" x2="380" y2="740"/><line x1="374" y1="810" x2="380" y2="810"/><line x1="374" y1="880" x2="380" y2="880"/><line x1="374" y1="949" x2="380" y2="949"/>
        <line x1="536" y1="949" x2="536" y2="955"/><line x1="692" y1="949" x2="692" y2="955"/><line x1="849" y1="949" x2="849" y2="955"/><line x1="1005" y1="949" x2="1005" y2="955"/><line x1="1162" y1="949" x2="1162" y2="955"/><line x1="1318" y1="949" x2="1318" y2="955"/><line x1="1475" y1="949" x2="1475" y2="955"/>
      </g>
      <g text-anchor="end">
        <text x="371" y="681">80</text><text x="371" y="744">60</text><text x="371" y="814">40</text><text x="371" y="884">20</text><text x="371" y="953">0</text>
      </g>
      <g text-anchor="middle">
        <text x="380" y="966">Apr 7</text><text x="536" y="966">Apr 8</text><text x="692" y="966">Apr 9</text><text x="849" y="966">Apr 10</text><text x="1005" y="966">Apr 11</text><text x="1162" y="966">Apr 12</text><text x="1318" y="966">Apr 13</text><text x="1457" y="966">Apr 14</text>
      </g>
    </svg>
    <div class="legend"><span><i style="background:var(--orange)"></i>Spam</span><span><i style="background:var(--red)"></i>Phishing</span></div>
  </section>

  <section class="actions">
    <div class="action">
      <svg class="ic" viewBox="0 0 24 24"><rect x="2" y="3" width="20" height="5"/><path d="M4 8v12h16V8M10 12h4"/></svg>
      <svg class="arrow" viewBox="0 0 24 24"><path d="M4 12h16M13 5l7 7-7 7"/></svg>
      <h3 class="serif">Review Quarantine</h3>
      <p>47 emails waiting for review</p>
    </div>
    <div class="action">
      <svg class="ic" viewBox="0 0 24 24"><path d="M14 2H6a2 2 0 0 0-2 2v16a2 2 0 0 0 2 2h12a2 2 0 0 0 2-2V8z"/><path d="M14 2v6h6M8 13h8M8 17h8"/></svg>
      <svg class="arrow" viewBox="0 0 24 24"><path d="M4 12h16M13 5l7 7-7 7"/></svg>
      <h3 class="serif">View Mail Log</h3>
      <p>All processed emails</p>
    </div>
  </section>
</main>
</body>
</html>
```